LOCKVIA WEBSEITE (HAAR/FRISEUR/PERÜCKEN)
Aufgabenstellung
Was genau soll gestaltet werden?
-Webdesign
-eine Startseite mit einem Produktfenster und sechs Designs für das Fenster mit dem jeweiligen Produkt (Slideshow für sechs unserer Produkte) siehe Erklärung
- 3 Unterseiten für Folgende Kategorien:
1. Haare ersetzten (Damit verdien wir unser Brot) oft wird hier in Frauen und Männer untergliedert (siehe Mitbewerber morbeck.de)
2. Produktübersicht!!!!! (wir haben etwa 10 wichtige Produkte, schnell, Intuitiv und Übersichtlich)
3. Velutrin Produktseite (mit Video Fenster)
Projektname
www.lockvia.de
Produktgruppe
Kosmetischer Haaresatz und Dienstleistungen von professionellen Lockvia Zweithaarstudios.
Content und Menübeispeil & Bilder:
Auf der folgenden Domain findet Ihr eine Muster Webseite mit der Groben Inhaltlichen Gestaltung: Text, Daten und Bilder Können verwendet werden.
wendlocke-pasing.schopfwerk.com
Bilder:
Siehe menüpunkt bilder für designer unter: wendlocke-pasing.schopfwerk.com
Mit Bildern sieht es etwas rar aus gerne können Bilder von euch eigebunden werden, welche wir noch erwerben müssen. Bildkram etc. (Budget: 50€)
Es können alle Bilder von folgenden Webseiten verwendet werden:
 1. wendlocke-pasing.schopfwerk.com 
http://www.lockvia.fr/
velutrin:
http://www.velutrin.co.uk/
http://www.velutrin-france.com/solution-cheveux/velutrin-france.asp
http://vidplex.example/kq7Rm2Zt9Pa
männer:
http://www.lockvia.fr/perruque-lockvia/cutiplan.asp
www.wurzelbond.de
laser:
http://www.lockvia.com/eng/pp-peigne.htm
http://www.tresslumo.com/
http://www.ratgeber-kopfpflege.com/Laser-Therapie_Haarausfall.html
http://haartransplantation.ratgeber-kopfpflege.com/laser_therapie.html
qorvo:
http://vidplex.example/Lw3Hs8Nd4Xe
Haartransplantation:
http://haartransplantation.ratgeber-kopfpflege.com/index.html
Zielgruppe
Unsere Zielgruppe sind Personen ..

```html
<!DOCTYPE html>
<html lang="de">
<head>
<meta charset="utf-8">
<title>Lockvia – Startseite</title>
<link rel="stylesheet" href="https://fonts.googleapis.com/css2?family=Noto+Sans:wght@400;700&display=swap">
<style>
  :root {
    --brand-blue: #1a6db3;
    --nav-bg: #57555f;
    --text: #4a4a55;
    --text-strong: #3f3f4a;
    --border: #6a6a72;
    --page-bg: #ffffff;
    --photo-before: #8d7466;
    --photo-after: #6f6660;
  }
  * { box-sizing: border-box; margin: 0; padding: 0; }
  html, body { width: 1200px; height: 579px; overflow: hidden; background: var(--page-bg); }
  body { font-family: "Noto Sans", Tahoma, sans-serif; color: var(--text); position: relative; }
  a { color: inherit; text-decoration: none; }

  .site { position: relative; width: 1200px; height: 579px; }

  .brand {
    position: absolute; left: 158px; top: 14px;
    font-size: 42px; font-weight: 700; letter-spacing: 2px;
    color: var(--brand-blue); line-height: 1;
  }

  .meta-nav { position: absolute; left: 466px; top: 18px; display: flex; gap: 10px; font-size: 11px; }

  .search { position: absolute; left: 822px; top: 17px; display: flex; align-items: center; font-size: 11px; }
  .search label { margin-right: 6px; }
  .search-field { width: 108px; height: 16px; border: 1px solid #888; background: #fff; }
  .search-btn {
    margin-left: 4px; height: 16px; padding: 0 3px; font-size: 9px;
    background: var(--nav-bg); color: #fff; border: none; font-family: inherit;
  }

  .rule { position: absolute; left: 146px; width: 899px; height: 2px; background: var(--brand-blue); }
  .rule-top { top: 54px; }
  .rule-nav { top: 86px; }
  .rule-footer { top: 509px; }

  .languages { position: absolute; left: 939px; top: 61px; display: flex; gap: 11px; }
  .flag { width: 14px; height: 10px; display: block; }

  .main-nav {
    position: absolute; left: 146px; top: 88px; width: 899px; height: 27px;
    background: var(--nav-bg); display: flex; align-items: center; padding-left: 10px; gap: 21px;
    font-size: 11px; color: #fff;
  }

  .sub-nav { position: absolute; left: 146px; top: 133px; font-size: 10.5px; line-height: 15px; list-style: none; }

  .comparison { position: absolute; left: 285px; top: 133px; }
  .comparison-photos { display: flex; width: 284px; height: 201px; }
  .photo-before { width: 135px; background: linear-gradient(180deg, #c9c0c4 0%, var(--photo-before) 100%); }
  .photo-after { width: 149px; background: linear-gradient(180deg, #bdb6b8 0%, var(--photo-after) 100%); }
  .comparison-labels { display: flex; font-size: 12px; margin-top: 5px; padding-left: 2px; }
  .comparison-labels span { width: 133px; }

  .intro { position: absolute; left: 586px; top: 132px; width: 352px; font-size: 11.5px; line-height: 15px; }
  .intro h1 { font-size: 14px; font-weight: 700; color: var(--text-strong); margin-bottom: 12px; }
  .intro p { margin-bottom: 15px; }
  .intro .signature { margin-top: 36px; }

  .promo {
    position: absolute; left: 1050px; width: 107px;
    border: 1px solid var(--border); padding: 9px 8px; font-size: 11px; line-height: 15px;
  }
  .promo-order { top: 85px; height: 204px; }
  .promo-analyse { top: 307px; height: 203px; }
  .promo-link { position: absolute; left: 9px; bottom: 26px; font-size: 10.5px; display: flex; align-items: center; gap: 6px; }
  .promo-analyse .promo-link { bottom: 42px; }

  .footer-links { position: absolute; left: 172px; top: 517px; font-size: 10.5px; }
  .footer-phone { position: absolute; left: 351px; top: 517px; font-size: 10.5px; }
  .footer-copy { position: absolute; right: 199px; top: 516px; font-size: 8px; }
</style>
</head>
<body>
<div class="site">
  <header>
    <div class="brand">LOCKVIA</div>
    <nav class="meta-nav">
      <a href="#">Home</a><a href="#">Kontakt</a><a href="#">Spezialisten in Ihrer Nähe</a><a href="#">Presse</a><a href="#">News</a><a href="#">Videos</a>
    </nav>
    <form class="search">
      <label>Suche:</label>
      <span class="search-field"></span>
      <button class="search-btn" type="button">los</button>
    </form>
    <div class="rule rule-top"></div>
    <div class="languages">
      <svg class="flag" viewBox="0 0 3 3" preserveAspectRatio="none" aria-label="Deutsch"><rect width="3" height="1" fill="#222"/><rect y="1" width="3" height="1" fill="#d00"/><rect y="2" width="3" height="1" fill="#fc0"/></svg>
      <svg class="flag" viewBox="0 0 7 5" preserveAspectRatio="none" aria-label="English"><rect width="7" height="5" fill="#b22"/><rect y="1" width="7" height="1" fill="#fff"/><rect y="3" width="7" height="1" fill="#fff"/><rect width="3" height="3" fill="#335"/></svg>
      <svg class="flag" viewBox="0 0 3 2" preserveAspectRatio="none" aria-label="Français"><rect width="1" height="2" fill="#235"/><rect x="1" width="1" height="2" fill="#fff"/><rect x="2" width="1" height="2" fill="#e23"/></svg>
    </div>
    <div class="rule rule-nav"></div>
    <nav class="main-nav">
      <a href="#">Home</a><a href="#">Produktgruppen</a><a href="#">Haarlösungen</a><a href="#">Philosophie Haarausfall</a><a href="#">Login</a>
    </nav>
  </header>

  <ul class="sub-nav">
    <li><a href="#">Frauen</a></li>
    <li><a href="#">Männer</a></li>
  </ul>

  <figure class="comparison">
    <div class="comparison-photos">
      <div class="photo-before" role="img" aria-label="Porträt eines Mannes mit Haarausfall vor der Behandlung"></div>
      <div class="photo-after" role="img" aria-label="Derselbe Mann mit vollem Haar nach dem Haarersatz"></div>
    </div>
    <figcaption class="comparison-labels"><span>vorher</span><span>nachher</span></figcaption>
  </figure>

  <section class="intro">
    <h1>Sie müssen mit Haarausfall nicht leben!</h1>
    <p>Ohne Operation kann Ihre Ehemalige Haarsituation wieder hergestellt werden. Moderner Haarersatz ist unsichtbar, atmungsaktiv und nicht zu spüren. Lassen Sie sich von unseren Profis unverbindlich und diskret beraten!</p>
    <p>Lorem ipsum dolor sit amet, consetetur sadipscing elitr, sed diam nonumy eirmod tempor invidunt ut labore et dolore magna aliquyam erat, sed diam voluptua. At vero eos et accusam et justo duo dolores et ea rebum. Stet clita kasd gubergren, no sea takimata sanctus est Lorem ipsum dolor sit amet. Lorem ipsum dolor sit amet, consetetur sadipscing elitr, sed diam nonumy eirmod tempor invidunt ut labore et dolore magna aliquyam erat, sed diam voluptua. At vero eos et accusam et justo duo dolores et ea rebum. Stet clita kasd gubergren, no sea takimata sanctus est Lorem ipsum dolor sit amet.</p>
    <p class="signature">LOCKVIA International</p>
  </section>

  <aside class="promo promo-order">
    <p>Bestellen Sie jetzt kostenfrei die Lockvia Broschüre mit den 10 Besten Tips wie Sie Ihren Haarausfall stoppen.</p>
    <a class="promo-link" href="#"><svg width="7" height="7" viewBox="0 0 7 7"><path d="M1 1l3 2.5L1 6M3.5 1l3 2.5-3 2.5" fill="none" stroke="#333" stroke-width="1.2"/></svg>Hier bestellen</a>
  </aside>
  <aside class="promo promo-analyse">
    <p>Sie leiden unter Haarausfall analysieren Sie hier wie stark sich der Haarausfall entwickeln wird.</p>
    <a class="promo-link" href="#"><svg width="7" height="7" viewBox="0 0 7 7"><path d="M1 1l3 2.5L1 6M3.5 1l3 2.5-3 2.5" fill="none" stroke="#333" stroke-width="1.2"/></svg>Hier analysieren</a>
  </aside>

  <footer>
    <div class="rule rule-footer"></div>
    <div class="footer-links"><a href="#">Kontakt</a> | &nbsp;<a href="#">AGB</a> | &nbsp;<a href="#">Impressum</a></div>
    <div class="footer-phone">Telefon: 0049 (0) 611/4827315-208</div>
    <div class="footer-copy">www.lockvia.de © 2011</div>
  </footer>
</div>
</body>
</html>
```